Oil and Gas Exploration and Production company needs a business card design

We need a business card design using our logo and colors in the logo. We want a mainstream design.

```html
<!DOCTYPE html>
<html lang="en">
<head>
<meta charset="utf-8">
<title>Solara Oil &amp; Gas – Business Cards</title>
<link rel="stylesheet" href="https://fonts.googleapis.com/css2?family=Arimo:wght@400;700&display=swap">
<style>
  :root {
    --backdrop: #d6d6d6;
    --card-white: #ffffff;
    --card-black: #0d0d0d;
    --gold: #c9a03a;
    --ink: #141414;
    --body-grey: #2a2a2a;
    --faint-mark: #ececec;
  }
  * { margin: 0; padding: 0; box-sizing: border-box; }
  html, body { width: 988px; height: 1200px; overflow: hidden; }
  body {
    background: var(--backdrop);
    font-family: "Arimo", Arial, sans-serif;
    position: relative;
  }
  .card {
    position: absolute;
    left: 90px;
    width: 807px;
    background: var(--card-white);
    overflow: hidden;
    box-shadow: 0 3px 10px rgba(0,0,0,0.18);
  }
  .card--front { top: 31px; height: 506px; }
  .card--back  { top: 684px; height: 465px; }
  .card__shapes { position: absolute; inset: 0; }

  .wordmark {
    position: absolute;
    display: flex;
    align-items: center;
    gap: 12px;
    color: var(--ink);
    font-weight: 700;
  }
  .wordmark__dot {
    width: 40px; height: 40px;
    border-radius: 50%;
    background: var(--gold);
    flex: none;
  }
  .wordmark__text { display: flex; flex-direction: column; line-height: 1; }
  .wordmark__name { font-size: 94px; letter-spacing: -2px; }
  .wordmark__tag  { font-size: 33px; letter-spacing: 5px; margin-top: 6px; padding-left: 4px; }

  .card--front .wordmark { left: 52px; top: 206px; }
  .card--back  .wordmark { left: 42px; top: 52px; }

  .contact { position: absolute; font-size: 21px; line-height: 1.33; }
  .contact__name { color: var(--gold); font-weight: 700; font-size: 28px; }
  .contact__role { font-size: 21px; }
  .label { color: var(--gold); }

  .card--front .contact {
    right: 46px; top: 110px;
    text-align: right;
    color: #fff;
  }
  .card--front .contact__role { margin-top: 2px; }
  .card--front .contact__address { margin-top: 62px; }
  .card--front .contact__phones { margin-top: 31px; }
  .card--front .contact__online { margin-top: 30px; }

  .card--back .contact {
    left: 45px; top: 215px;
    color: var(--body-grey);
  }
  .card--back .contact__role { margin-top: 6px; }
  .card--back .contact__address { margin-top: 30px; }
  .card--back .contact p { line-height: 1.38; }
</style>
</head>
<body>

<section class="card card--front" aria-label="Business card, front">
  <svg class="card__shapes" viewBox="0 0 807 506" width="807" height="506" aria-hidden="true">
    <circle class="faint-mark" cx="191" cy="335" r="130" fill="var(--faint-mark)"/>
    <polygon class="accent-stripe" points="340,0 807,0 807,506 460,506" fill="var(--gold)"/>
    <polygon class="dark-panel" points="352,0 807,0 807,506 472,506" fill="var(--card-black)"/>
  </svg>

  <div class="wordmark">
    <span class="wordmark__dot"></span>
    <span class="wordmark__text">
      <span class="wordmark__name">Solara</span>
      <span class="wordmark__tag">OIL &amp; GAS</span>
    </span>
  </div>

  <div class="contact">
    <p class="contact__name">Dana L. Whitford</p>
    <p class="contact__role">Partner</p>
    <div class="contact__address">
      <p>82 Meridian Street</p>
      <p>Fresno, California 93721</p>
    </div>
    <div class="contact__phones">
      <p><span class="label">Tel:</span> 555.214.0193</p>
      <p><span class="label">Fax:</span> 555.214.0194</p>
    </div>
    <div class="contact__online">
      <p><span class="label">Email:</span> dana@solara.com</p>
      <p><span class="label">Web:</span> www.solara.com</p>
    </div>
  </div>
</section>

<section class="card card--back" aria-label="Business card, alternate layout">
  <svg class="card__shapes" viewBox="0 0 807 465" width="807" height="465" aria-hidden="true">
    <circle class="feature-disc" cx="690" cy="300" r="150" fill="var(--card-black)"/>
  </svg>

  <div class="wordmark">
    <span class="wordmark__dot"></span>
    <span class="wordmark__text">
      <span class="wordmark__name">Solara</span>
      <span class="wordmark__tag">OIL &amp; GAS</span>
    </span>
  </div>

  <div class="contact">
    <p class="contact__name">Dana L. Whitford</p>
    <p class="contact__role">Partner</p>
    <div class="contact__address">
      <p>82 Meridian Street</p>
      <p>Fresno, California 93721</p>
      <p><span class="label">Tel:</span> 555.214.0193, <span class="label">Fax:</span> 555.214.0194</p>
      <p><span class="label">Email:</span> dana@solara.com, <span class="label">Web:</span> www.solara.com</p>
    </div>
  </div>
</section>

</body>
</html>
```